Water ATM Card

Need a design for water ATM cards. Size of card is 3.375 x 2.125 inch
On the Front include the Cedar brook Logo.
Bottom right corner should have Price $100
On the Back
This card is to be used to access water refills at any Cedar Brook Water Vending Machines.
Please contact (869) 614 2938 or (869) 731 4072 or email clearflowhq@examplemail.com for any assistance or recharging of card.

```html
<!DOCTYPE html>
<html lang="en">
<head>
<meta charset="utf-8">
<title>Cedar Brook – Water ATM Card</title>
<link rel="stylesheet" href="https://fonts.googleapis.com/css2?family=Montserrat:wght@400;500;600;700;800&family=Nunito:wght@400;600&display=swap">
<style>
  :root {
    --stage: #939598;
    --white: #ffffff;
    --ink: #111111;
    --brand-blue: #1a75bb;
    --banner-top: #2278c2;
    --banner-bottom: #1a55a0;
    --navy: #283593;
    --sky: #239bd8;
    --deep: #22449a;
    --green-light: #84c341;
    --green-deep: #16994a;
    --water-light: #d8ecf8;
    --water-mid: #6fb2e0;
    --water-dark: #1d5fae;
    --soft-text: #dde8f6;
  }
  * { box-sizing: border-box; margin: 0; padding: 0; }
  html, body { width: 1115px; height: 1200px; overflow: hidden; }
  body {
    background: var(--stage);
    position: relative;
    font-family: "Montserrat", sans-serif;
  }
  .side-label {
    position: absolute;
    left: 84px;
    font-family: "Nunito", sans-serif;
    font-size: 30px;
    color: var(--ink);
  }
  .side-label.front { top: 310px; }
  .side-label.back { top: 850px; }

  .card {
    position: absolute;
    left: 247px;
    width: 754px;
    height: 474px;
    overflow: hidden;
    background: var(--white);
  }
  .card.front { top: 93px; }
  .card.back { top: 633px; }

  /* Front */
  .title-banner {
    position: absolute;
    left: 106px; top: 33px;
    width: 540px; height: 65px;
    background: linear-gradient(var(--banner-top), var(--banner-bottom));
    color: var(--white);
    font-size: 52px;
    font-weight: 400;
    line-height: 65px;
    text-align: center;
    letter-spacing: 0.5px;
  }
  .title-banner strong { font-weight: 800; }
  .brand-name {
    position: absolute;
    left: 0; right: 0; top: 206px;
    text-align: center;
    font-size: 38px;
    font-weight: 800;
    color: var(--brand-blue);
    letter-spacing: 1px;
  }
  .water-art { position: absolute; left: 0; top: 0; }
  .base-bar {
    position: absolute;
    left: 0; bottom: 0;
    width: 100%; height: 18px;
    background: var(--navy);
  }
  .price-tag { position: absolute; left: 0; top: 0; }
  .price-text {
    position: absolute;
    left: 581px; top: 338px;
    width: 140px;
    text-align: center;
    color: var(--white);
    font-weight: 700;
    line-height: 1;
  }
  .price-text .label { font-size: 21px; display: block; }
  .price-text .amount { font-size: 40px; display: block; margin-top: 2px; letter-spacing: -1px; }

  /* Back */
  .band-top {
    position: absolute; left: 0; top: 0; width: 100%; height: 52px;
    background: linear-gradient(100deg, var(--sky), #1c6ab4);
  }
  .band-green {
    position: absolute; left: 0; top: 52px; width: 100%; height: 109px;
    background: linear-gradient(90deg, var(--green-light), var(--green-deep));
  }
  .band-info {
    position: absolute; left: 0; top: 161px; width: 100%; height: 208px;
    background: linear-gradient(160deg, #2a8fd2, #1c6bb5 50%, var(--deep));
  }
  .chip-panel {
    position: absolute; left: 50px; top: 205px;
    width: 99px; height: 84px;
    background: var(--white);
    border-radius: 15px;
  }
  .card-note {
    position: absolute; left: 184px; top: 220px;
    width: 500px;
    font-size: 14.5px;
    line-height: 18.6px;
    font-weight: 500;
    color: var(--soft-text);
  }
  .contact-tab { position: absolute; left: 0; top: 0; }
  .contact-heading {
    position: absolute; left: 241px; top: 339px; width: 270px;
    text-align: center;
    font-size: 21px; font-weight: 500;
    color: var(--navy);
  }
  .contact-row {
    position: absolute; top: 389px;
    display: flex; align-items: center; gap: 9px;
    font-family: "Nunito", sans-serif;
    color: var(--ink);
  }
  .contact-row.phone { left: 27px; font-size: 21px; }
  .contact-row.mail { left: 428px; font-size: 19px; }
  .contact-row svg { flex: none; }
  .contact-footnote {
    position: absolute; left: 0; right: 0; top: 427px;
    text-align: center;
    font-family: "Nunito", sans-serif;
    font-size: 20px;
    color: var(--ink);
  }
</style>
</head>
<body>
  <div class="side-label front">Front</div>
  <div class="side-label back">Back</div>

  <section class="card front">
    <svg class="water-art" width="754" height="474" viewBox="0 0 754 474" role="img" aria-label="Photo of splashing clear blue water across the lower card">
      <defs>
        <linearGradient id="waterFill" x1="0" y1="0" x2="0" y2="1">
          <stop offset="0" stop-color="var(--water-mid)"/>
          <stop offset="0.45" stop-color="var(--water-light)"/>
          <stop offset="1" stop-color="#a9d2ee"/>
        </linearGradient>
        <linearGradient id="waterEdge" x1="0" y1="0" x2="1" y2="0">
          <stop offset="0" stop-color="var(--water-dark)" stop-opacity="0.75"/>
          <stop offset="0.45" stop-color="var(--water-dark)" stop-opacity="0.15"/>
          <stop offset="1" stop-color="var(--water-dark)" stop-opacity="0.35"/>
        </linearGradient>
      </defs>
      <path d="M0 162 C30 170 60 190 80 260 C110 300 150 300 200 305 C260 300 300 290 360 292 C420 294 470 300 520 300 C590 305 640 320 700 318 C725 316 745 305 754 300 L754 474 L0 474 Z" fill="url(#waterFill)"/>
      <path d="M0 162 C30 170 60 190 80 260 C110 300 150 300 200 305 C260 300 300 290 360 292 C420 294 470 300 520 300 C590 305 640 320 700 318 C725 316 745 305 754 300 L754 474 L0 474 Z" fill="url(#waterEdge)"/>
    </svg>

    <h1 class="title-banner">WATER <strong>ATM</strong> CARD</h1>
    <div class="brand-name">CEDAR BROOK</div>

    <svg class="price-tag" width="754" height="474" viewBox="0 0 754 474" aria-hidden="true">
      <defs>
        <linearGradient id="tagFill" x1="0" y1="0" x2="1" y2="1">
          <stop offset="0" stop-color="var(--green-light)"/>
          <stop offset="1" stop-color="var(--green-deep)"/>
        </linearGradient>
      </defs>
      <path d="M646 310 C636 290 638 262 644 250 C650 242 656 248 655 262 C654 285 652 305 651 314" fill="none" stroke="var(--navy)" stroke-width="1.5"/>
      <rect x="601" y="324" width="100" height="100" rx="8" transform="rotate(45 651 374)" fill="url(#tagFill)"/>
      <circle cx="651" cy="314" r="3.5" fill="var(--white)" stroke="var(--navy)" stroke-width="1"/>
    </svg>
    <div class="price-text"><span class="label">PRICE</span><span class="amount">$100</span></div>

    <div class="base-bar"></div>
  </section>

  <section class="card back">
    <div class="band-top"></div>
    <div class="band-green"></div>
    <div class="band-info"></div>
    <div class="chip-panel"></div>
    <p class="card-note">Lorem ipsum dolor sit amet, consectetuer adipiscing elit, sed diam nonummy nibh euismod tincidunt ut laoreet dolore magna aliquam erat volutpat.</p>

    <svg class="contact-tab" width="754" height="474" viewBox="0 0 754 474" aria-hidden="true">
      <polygon points="241,370 272,331 480,331 511,370" fill="var(--white)"/>
    </svg>
    <div class="contact-heading">PLEASE CONTACT</div>

    <div class="contact-row phone">
      <svg width="34" height="34" viewBox="0 0 34 34" aria-hidden="true">
        <rect x="7" y="7" width="20" height="20" transform="rotate(45 17 17)" fill="var(--green-deep)"/>
        <path d="M13 11 l3 3 -2 2 c1 2 2 3 4 4 l2 -2 3 3 -2 2 c-5 -1 -9 -5 -10 -10 z" fill="var(--white)"/>
      </svg>
      <span>(869) 614 2938, (869) 731 4072</span>
    </div>
    <div class="contact-row mail">
      <svg width="34" height="34" viewBox="0 0 34 34" aria-hidden="true">
        <rect x="7" y="7" width="20" height="20" transform="rotate(45 17 17)" fill="var(--green-deep)"/>
        <rect x="11" y="13" width="12" height="9" fill="none" stroke="var(--white)" stroke-width="1.5"/>
        <path d="M11 13 l6 5 6 -5" fill="none" stroke="var(--white)" stroke-width="1.5"/>
      </svg>
      <span>clearflowhq@examplemail.com</span>
    </div>
    <div class="contact-footnote">For any Assistance or Recharging of Card</div>
  </section>
</body>
</html>
```